Real Estate For Sale Sign

I need to design a for sale sign. It needs to include The following information
Logo: Attached
Name: Corinne Vasquel,
Company Name: Gilded Harbor Real Estate,
Phone Number: 503-841-2096
BRE Licence Number 04817359 (Can Be small)
Sign size 24x30

I am not sure about including my website but I would like to see options with it. www.gildedharbor-example.com
Updates

Target Market(s)

Potential Buyers or Sellers of Real Estate. Must be easy to read.

Industry/Entity Type

Real Estate

Requirements
Must have
• I want it to feel luxurious and sharp.

```html
<!DOCTYPE html>
<html lang="en">
<head>
<meta charset="utf-8">
<title>Gilded Harbor Real Estate – For Sale Sign</title>
<link rel="stylesheet" href="https://fonts.googleapis.com/css2?family=Arvo:wght@700&family=Bitter:wght@400;700&display=swap">
<style>
  :root {
    --backdrop: #e9ecef;
    --sign-white: #ffffff;
    --header-black: #050505;
    --bar-black: #0b0b0b;
    --accent-blue: #1f8fea;
    --headline-blue: #2a9df4;
    --headline-shade: #0b3563;
    --panel-blue-light: #14b4f0;
    --panel-blue-dark: #1c7fcf;
    --on-dark: #ffffff;
  }
  * { box-sizing: border-box; margin: 0; padding: 0; }
  html, body {
    width: 1200px; height: 772px; overflow: hidden;
    background: var(--backdrop);
  }
  .canvas { position: relative; width: 1200px; height: 772px; }
  .sign {
    position: absolute; left: 320px; top: 36px;
    width: 560px; height: 700px;
    background: var(--sign-white);
    box-shadow: 0 6px 24px rgba(0,0,0,0.18);
  }
  .sign-header {
    position: absolute; left: 0; top: 0; width: 100%; height: 135px;
    background: var(--header-black);
    display: flex; align-items: center; padding-left: 30px;
  }
  .company-name {
    font-family: "Bitter", Georgia, serif;
    font-weight: 400; font-size: 22px; letter-spacing: 1px;
    color: var(--on-dark);
  }
  .accent-band {
    position: absolute; left: 0; top: 154px; width: 100%; height: 20px;
    background: var(--accent-blue);
  }
  .headline {
    position: absolute; left: 0; top: 300px; width: 100%;
    text-align: center;
    font-family: "Arvo", "Rockwell", serif; font-weight: 700;
    font-size: 84px; letter-spacing: 4px; line-height: 1;
    color: var(--headline-blue);
    text-shadow: 2px 2px 0 var(--headline-shade), 4px 4px 0 var(--headline-shade), 6px 7px 8px rgba(0,0,0,0.35);
  }
  .web-bar {
    position: absolute; left: 0; top: 542px; width: 100%; height: 20px;
    background: var(--bar-black);
    display: flex; align-items: center; justify-content: flex-end; padding-right: 30px;
  }
  .website {
    font-family: "Bitter", Georgia, serif; font-weight: 700;
    font-size: 11px; letter-spacing: 1px; color: var(--on-dark);
  }
  .contact-panel {
    position: absolute; left: 0; top: 582px; width: 100%; height: 118px;
    background: linear-gradient(90deg, var(--panel-blue-light), var(--panel-blue-dark));
    text-align: right; padding: 8px 32px 0 0;
    font-family: "Bitter", Georgia, serif; color: var(--on-dark);
  }
  .phone { font-weight: 700; font-size: 30px; letter-spacing: 1.5px; line-height: 38px; }
  .agent-name { font-weight: 700; font-size: 29px; letter-spacing: 1.5px; line-height: 38px; }
  .licence { font-weight: 400; font-size: 17px; letter-spacing: 1px; line-height: 26px; }
</style>
</head>
<body>
<main class="canvas">
  <section class="sign" aria-label="Gilded Harbor Real Estate for sale sign">
    <header class="sign-header">
      <span class="company-name">Gilded Harbor Real Estate</span>
    </header>
    <div class="accent-band"></div>
    <h1 class="headline">FOR SALE</h1>
    <div class="web-bar"><span class="website">www.gildedharbor-example.com</span></div>
    <div class="contact-panel">
      <p class="phone">503-841-2096</p>
      <p class="agent-name">Corinne Vasquel</p>
      <p class="licence">BRE#04817359</p>
    </div>
  </section>
</main>
</body>
</html>
```